Small Ecommerce Styled Site to Sell / Lease Domain Names

We have a small portfolio of 100+ domain names that we would like to offer for sale or lease via a web site. Along the lines of http://www.velramarkets.com/searchdomain.html?priceChoice=2&sort=leasing_desc

We would like initially a 4 page design, listing page (as site referenced above), domain info page (Universal Domain Name Landing Page with form) and checkout a page and About Us Page

We do not want a replica of the site listed, please use it as a guide only, we are looking for a fresh design, in similar concept web 2.0

Our Colours are #351a41 (Main) - #ffca27 (Secondary) all other colours must compliment those 2.
Updates

Domain Landing Page:  I am sorry I was not clear about expectations, however we would like a domain landing page that would be the default holding page for a domain name.

For some examples of what I mean please see:
https://www.pobexhub.com.au/guest-articles/7626-domain-for-sale-landing-pages.html
http://dev.quillterbrokers.com/blog/2013/09/sales-only-landers-and-buy-it-now-2/

Industry/Entity Type

Domain

Font styles to use
Sans Serif

```html
<!DOCTYPE html>
<html lang="en">
<head>
<meta charset="utf-8">
<title>Domains For Sale</title>
<link rel="stylesheet" href="https://fonts.googleapis.com/css2?family=Ubuntu:wght@300;400;500&display=swap">
<style>
:root{
  --plum:#351a41;
  --plum-deep:#2a1434;
  --plum-soft:#5a3a6b;
  --lilac:#dccbe6;
  --lilac-pale:#f8f3fb;
  --gold:#ffca27;
  --gold-deep:#f2b400;
  --sky:#2b9cf0;
  --ink:#2c2330;
  --muted:#6f6675;
  --line:#e6dcc0;
  --white:#fff;
}
*{box-sizing:border-box;margin:0;padding:0}
html,body{width:786px;height:1200px;overflow:hidden}
body{position:relative;font-family:"Ubuntu",sans-serif;color:var(--ink);background:var(--white);font-size:12px}
svg.ic{width:12px;height:12px;flex:none}

.topbar{position:absolute;left:0;top:0;width:786px;height:30px;background:var(--plum-deep);display:flex;justify-content:flex-end;z-index:2}
.topbar a{display:flex;align-items:center;gap:5px;padding:0 14px;color:var(--white);font-size:11px;text-decoration:none;border-left:1px solid #4b2f58;white-space:nowrap}
.topbar svg{fill:none;stroke:var(--gold);stroke-width:1.4}

.hero{position:absolute;left:0;top:30px;width:786px;height:222px;background:radial-gradient(ellipse at 50% 45%,#8a7297 0%,#6a4f79 45%,#45294f 100%)}
.hero-title{position:absolute;left:0;top:52px;width:786px;text-align:center;color:var(--white)}
.hero-title .tag{display:block;color:var(--gold);font-size:29px;font-weight:500;line-height:1}
.hero-title .name{display:block;font-size:48px;font-weight:500;line-height:1.05;margin-top:4px;letter-spacing:-.5px}
.hero-band{position:absolute;left:0;top:252px;width:786px;height:6px;background:var(--plum)}
.main-nav{position:absolute;left:186px;top:238px;width:430px;height:29px;background:linear-gradient(var(--gold),var(--gold-deep));border:1px solid #d9a400;border-radius:3px;display:flex;z-index:2}
.main-nav a{display:flex;align-items:center;justify-content:center;color:var(--plum);text-decoration:none;font-size:13px;border-right:1px solid #e0a800;white-space:nowrap}
.main-nav a:last-child{border-right:0}

.sidebox{position:absolute;left:18px;width:174px;background:var(--white);box-shadow:0 0 0 1px #ececec}
.sidebox h3{background:var(--plum);color:var(--white);font-weight:400;font-size:13px;padding:0 18px;display:flex;align-items:center}
.cats h3{height:32px;font-size:15px}
.cat{height:29px;display:flex;align-items:center;gap:8px;padding-left:4px;border-top:1px solid #ececec;font-size:11px;white-space:nowrap}
.cat svg{fill:var(--plum)}
.cat.active{background:#ececec;border-left:4px solid var(--gold);padding-left:15px}
.cat.sub{padding-left:35px;border-top:0}
.cat.sub.hot{color:var(--gold-deep)}
.ext h3,.price h3{height:25px}
.ext-grid{display:grid;grid-template-columns:repeat(3,1fr);row-gap:16px;padding:14px 6px 16px}
.chk{display:flex;align-items:center;gap:6px;font-size:11px;white-space:nowrap}
.chk i{width:12px;height:12px;background:#eeeedc;border:1px solid #d3d3c0;flex:none}
.range{display:flex;align-items:center;gap:4px;padding:12px 6px;font-size:11px;white-space:nowrap}
.range span.box{width:47px;height:18px;background:#eef0d8;border:1px solid #c9cbb0;text-align:center;color:#9a9a86;line-height:16px;margin-right:14px}
.side-search{position:absolute;left:17px;top:978px;width:176px;height:32px;background:linear-gradient(var(--gold),var(--gold-deep));border:1px solid #d9a400;border-radius:2px;color:var(--plum);font-size:19px;display:flex;align-items:center;justify-content:center}

.search{position:absolute;left:529px;top:295px;width:239px;height:27px;display:flex;border:1px solid #cfcfcf}
.search .field{flex:1;display:flex;align-items:center;gap:8px;padding-left:7px;color:#9c9c9c;font-size:11px;white-space:nowrap}
.search .field svg{fill:none;stroke:var(--plum);stroke-width:2}
.search .btn{width:54px;background:var(--plum);color:var(--white);display:flex;align-items:center;justify-content:center;font-size:12px}

.tabs{position:absolute;left:222px;top:338px;display:flex;gap:4px}
.tabs span{height:32px;display:flex;align-items:center;justify-content:center;font-size:15px;background:var(--gold);color:var(--plum);white-space:nowrap}
.tabs .on{background:var(--plum);color:var(--gold)}
.tabline{position:absolute;left:222px;top:370px;width:548px;height:5px;background:var(--plum)}

.listing{position:absolute;left:222px;top:375px;width:548px}
.row{display:grid;grid-template-columns:214px 170px 80px 84px;align-items:center;height:36.6px;border-bottom:1px solid var(--line);font-size:11px;white-space:nowrap}
.row:nth-child(odd){background:var(--lilac-pale)}
.row.head{height:27px;background:var(--lilac);border:0;font-size:12px}
.row .dom{padding-left:14px}
.row .cat-cell{display:flex;align-items:center;gap:7px;padding-left:8px}
.row .cat-cell svg{width:14px;height:12px;fill:none;stroke:var(--ink);stroke-width:1.3;flex:none}
.head .cat-cell{padding-left:54px}
.head .fee{padding-left:4px}
.head .pr{padding-left:22px}
.chip{display:inline-flex;align-items:center;gap:4px;height:19px;border-radius:3px;font-size:10.5px;padding:0 5px;white-space:nowrap;overflow:hidden}
.chip svg{fill:none;stroke-width:1.3}
.chip.lease{width:60px;background:var(--gold);border:1px solid #d9a400;color:var(--plum)}
.chip.lease svg{stroke:var(--plum)}
.chip.offer{width:80px;background:var(--plum);color:var(--gold)}
.chip.offer svg{stroke:var(--gold)}
.chip.buy{width:80px;background:var(--sky);color:var(--white);justify-content:center;gap:10px}
.chip.buy svg{stroke:var(--white)}

.pager{position:absolute;right:16px;top:943px;display:flex;gap:4px;align-items:center}
.pager span{width:19px;height:19px;border:1px solid #c8c8c8;border-radius:2px;background:linear-gradient(#fff,#e9e9e9);font-size:9px;display:flex;align-items:center;justify-content:center}
.pager .cur{background:var(--plum);color:var(--white);border-color:var(--plum)}
.pager .gap{border:0;background:none;width:14px}

.footer{position:absolute;left:0;top:1030px;width:786px;height:126px;background:var(--plum);border-top:2px solid var(--gold);display:flex}
.footer .col{padding:20px 0 0 17px;color:var(--white)}
.footer .col+.col{border-left:1px solid #4d3259}
.footer h4{font-weight:400;font-size:14px;margin-bottom:9px;white-space:nowrap}
.footer p{font-size:10.5px;font-weight:300;line-height:14px;color:#d8cddd;width:240px}
.footer ul{list-style:none;font-size:11px;color:#d8cddd}
.footer li{margin-bottom:7px}
.footer li::before{content:"›";color:var(--gold);margin-right:6px}
.social{display:flex;gap:6px}
.social i{width:28px;height:28px;background:var(--gold);display:block}
.copyright{position:absolute;left:16px;right:20px;top:1170px;font-size:10px;color:var(--plum)}
</style>
</head>
<body>
<svg width="0" height="0" style="position:absolute">
  <symbol id="user" viewBox="0 0 12 12"><circle cx="6" cy="4" r="2.6"/><path d="M1 11.5c.6-3 2.6-4.3 5-4.3s4.4 1.3 5 4.3z"/></symbol>
  <symbol id="cart" viewBox="0 0 12 12"><path d="M.5 1.5h2l1.4 6.5h6.3l1.3-4.8H3"/><circle cx="4.6" cy="10.3" r=".9"/><circle cx="9.3" cy="10.3" r=".9"/></symbol>
  <symbol id="help" viewBox="0 0 12 12"><circle cx="6" cy="6" r="5.3"/><path d="M4.3 4.6a1.8 1.8 0 1 1 2.4 1.7c-.5.2-.7.6-.7 1.2M6 8.8v.5"/></symbol>
  <symbol id="plus" viewBox="0 0 12 12"><path d="M6 0a6 6 0 1 0 .01 0zM5.2 3h1.6v2.2H9v1.6H6.8V9H5.2V6.8H3V5.2h2.2z" fill-rule="evenodd"/></symbol>
  <symbol id="laptop" viewBox="0 0 14 12"><rect x="2.5" y="1.5" width="9" height="6.5"/><path d="M.8 10.5h12.4l-1.5-2.5H2.3z"/></symbol>
  <symbol id="swap" viewBox="0 0 12 12"><path d="M1 3.5h9M7.5 1l2.5 2.5L7.5 6M11 8.5H2M4.5 6L2 8.5 4.5 11"/></symbol>
  <symbol id="tag" viewBox="0 0 12 12"><path d="M1 1h5l5 5-5 5-5-5z"/><circle cx="3.7" cy="3.7" r=".9"/></symbol>
  <symbol id="lens" viewBox="0 0 12 12"><circle cx="5" cy="5" r="3.5"/><path d="M7.6 7.6l3.4 3.4"/></symbol>
</svg>

<header class="topbar">
  <a href="#"><svg class="ic"><use href="#user"/></svg>Signup</a>
  <a href="#"><svg class="ic"><use href="#user"/></svg>Login</a>
  <a href="#"><svg class="ic"><use href="#cart"/></svg>Cart</a>
  <a href="#"><svg class="ic"><use href="#help"/></svg>FAQ</a>
</header>

<section class="hero" role="img" aria-label="Purple toned scene of scattered cubes labelled with domain extensions such as .com, .net, .org and .biz">
  <h1 class="hero-title"><span class="tag">For Sale</span><span class="name">YourDomainName.com</span></h1>
</section>
<div class="hero-band"></div>
<nav class="main-nav">
  <a href="#" style="width:108px">Buy Domains</a>
  <a href="#" style="width:126px">Lease Domains</a>
  <a href="#" style="width:106px">Categories</a>
  <a href="#" style="width:90px">About Us</a>
</nav>

<aside class="sidebox cats" style="top:294px">
  <h3>Categories</h3>
  <div class="cat" style="border-top:0"><svg class="ic"><use href="#plus"/></svg>Automotive</div>
  <div class="cat active">Business and Finance</div>
  <div class="cat sub">Women's Apparel</div>
  <div class="cat sub hot">Dresses</div>
  <div class="cat sub">Tops &amp; Blouses</div>
  <div class="cat sub">T-Shirts</div>
  <div class="cat"><svg class="ic"><use href="#plus"/></svg>Computers and Internet</div>
  <div class="cat"><svg class="ic"><use href="#plus"/></svg>Education</div>
  <div class="cat"><svg class="ic"><use href="#plus"/></svg>Entertainment</div>
  <div class="cat"><svg class="ic"><use href="#plus"/></svg>Family</div>
  <div class="cat"><svg class="ic"><use href="#plus"/></svg>Food and Beverage</div>
  <div class="cat"><svg class="ic"><use href="#plus"/></svg>Food and Beverage</div>
  <div class="cat"><svg class="ic"><use href="#plus"/></svg>Food and Beverage</div>
  <div class="cat"><svg class="ic"><use href="#plus"/></svg>Food and Beverage</div>
</aside>

<aside class="sidebox ext" style="top:749px">
  <h3>Extensions</h3>
  <div class="ext-grid">
    <span class="chk"><i></i>All</span><span class="chk"><i></i>.com</span><span class="chk"><i></i>.net</span>
    <span class="chk"><i></i>.info</span><span class="chk"><i></i>.org</span><span class="chk"><i></i>.co.uk</span>
    <span class="chk"><i></i>.co.za</span><span class="chk"><i></i>.es</span><span class="chk"><i></i>.de</span>
  </div>
</aside>

<aside class="sidebox price" style="top:890px">
  <h3>Price Range</h3>
  <div class="range">Min: <span class="box">0</span>Max: <span class="box">0</span></div>
</aside>
<div class="side-search">SEARCH</div>

<div class="search">
  <div class="field"><svg class="ic"><use href="#lens"/></svg>Enter Keyword or Domain</div>
  <div class="btn">Search</div>
</div>

<div class="tabs">
  <span class="on" style="width:160px">Premium Domains</span>
  <span style="width:144px">Lease Domains</span>
  <span style="width:120px">Buy Domains</span>
</div>
<div class="tabline"></div>

<div class="listing">
  <div class="row head"><span class="dom">Domain Name</span><span class="cat-cell">Category</span><span class="fee">Lease Fee</span><span class="pr">Price</span></div>
  <div class="row"><span class="dom">BreezeChill.com</span><span class="cat-cell"><svg><use href="#laptop"/></svg>Computers and Internet</span><span><span class="chip lease"><svg class="ic"><use href="#swap"/></svg>$240</span></span><span><span class="chip offer"><svg class="ic"><use href="#tag"/></svg>Make Offer</span></span></div>
  <div class="row"><span class="dom">DuneHarbor.com</span><span class="cat-cell"><svg><use href="#laptop"/></svg>Computers and Internet</span><span><span class="chip lease"><svg class="ic"><use href="#swap"/></svg>$1240</span></span><span><span class="chip offer"><svg class="ic"><use href="#tag"/></svg>Make Offer</span></span></div>
  <div class="row"><span class="dom">DuneHarbor.com</span><span class="cat-cell"><svg><use href="#laptop"/></svg>Computers and Internet</span><span><span class="chip lease"><svg class="ic"><use href="#swap"/></svg>$1240</span></span><span><span class="chip offer"><svg class="ic"><use href="#tag"/></svg>Make Offer</span></span></div>
  <div class="row"><span class="dom">DuneHarbor.com</span><span class="cat-cell"><svg><use href="#laptop"/></svg>Computers and Internet</span><span></span><span><span class="chip buy"><svg class="ic"><use href="#cart"/></svg>$4,288</span></span></div>
  <div class="row"><span class="dom">DuneHarbor.com</span><span class="cat-cell"><svg><use href="#laptop"/></svg>Computers and Internet</span><span><span class="chip lease"><svg class="ic"><use href="#swap"/></svg>$1240</span></span><span><span class="chip offer"><svg class="ic"><use href="#tag"/></svg>Make Offer</span></span></div>
  <div class="row"><span class="dom">DuneHarbor.com</span><span class="cat-cell"><svg><use href="#laptop"/></svg>Computers and Internet</span><span><span class="chip lease"><svg class="ic"><use href="#swap"/></svg>$1240</span></span><span><span class="chip offer"><svg class="ic"><use href="#tag"/></svg>Make Offer</span></span></div>
  <div class="row"><span class="dom">DuneHarbor.com</span><span class="cat-cell"><svg><use href="#laptop"/></svg>Computers and Internet</span><span><span class="chip lease"><svg class="ic"><use href="#swap"/></svg>$1240</span></span><span><span class="chip offer"><svg class="ic"><use href="#tag"/></svg>Make Offer</span></span></div>
  <div class="row"><span class="dom">DuneHarbor.com</span><span class="cat-cell"><svg><use href="#laptop"/></svg>Computers and Internet</span><span><span class="chip lease"><svg class="ic"><use href="#swap"/></svg>$1240</span></span><span><span class="chip offer"><svg class="ic"><use href="#tag"/></svg>Make Offer</span></span></div>
  <div class="row"><span class="dom">DuneHarbor.com</span><span class="cat-cell"><svg><use href="#laptop"/></svg>Computers and Internet</span><span><span class="chip lease"><svg class="ic"><use href="#swap"/></svg>$1240</span></span><span><span class="chip offer"><svg class="ic"><use href="#tag"/></svg>Make Offer</span></span></div>
  <div class="row"><span class="dom">DuneHarbor.com</span><span class="cat-cell"><svg><use href="#laptop"/></svg>Computers and Internet</span><span><span class="chip lease"><svg class="ic"><use href="#swap"/></svg>$1240</span></span><span><span class="chip offer"><svg class="ic"><use href="#tag"/></svg>Make Offer</span></span></div>
  <div class="row"><span class="dom">BreezeChill.com</span><span class="cat-cell"><svg><use href="#laptop"/></svg>Computers and Internet</span><span><span class="chip lease"><svg class="ic"><use href="#swap"/></svg>$240</span></span><span><span class="chip offer"><svg class="ic"><use href="#tag"/></svg>Make Offer</span></span></div>
  <div class="row"><span class="dom">DuneHarbor.com</span><span class="cat-cell"><svg><use href="#laptop"/></svg>Computers and Internet</span><span><span class="chip lease"><svg class="ic"><use href="#swap"/></svg>$1240</span></span><span><span class="chip offer"><svg class="ic"><use href="#tag"/></svg>Make Offer</span></span></div>
  <div class="row"><span class="dom">DuneHarbor.com</span><span class="cat-cell"><svg><use href="#laptop"/></svg>Computers and Internet</span><span></span><span><span class="chip buy"><svg class="ic"><use href="#cart"/></svg>$5,288</span></span></div>
  <div class="row"><span class="dom">DuneHarbor.com</span><span class="cat-cell"><svg><use href="#laptop"/></svg>Computers and Internet</span><span><span class="chip lease"><svg class="ic"><use href="#swap"/></svg>$1240</span></span><span><span class="chip offer"><svg class="ic"><use href="#tag"/></svg>Make Offer</span></span></div>
</div>

<div class="pager">
  <span>‹</span><span>1</span><span>2</span><span>3</span><span class="cur">4</span><span>5</span><span class="gap">…</span><span>10</span><span>20</span><span>30</span><span>›</span>
</div>

<footer class="footer">
  <div class="col" style="width:282px">
    <h4>About Domain</h4>
    <p>It is a long established fact that a reader will be distracted by the readable content of a page when looking at its layout.</p>
  </div>
  <div class="col" style="width:228px;padding-left:29px">
    <h4>Domains For Sale</h4>
    <ul><li>yourdomainname.com</li><li>yourdomainname.com</li><li>yourdomainname.com</li></ul>
  </div>
  <div class="col" style="width:276px;padding-left:29px">
    <h4>Stay Connected With Us</h4>
    <div class="social"><i aria-label="Social link"></i><i aria-label="Social link"></i><i aria-label="Social link"></i><i aria-label="Social link"></i><i aria-label="Social link"></i></div>
  </div>
</footer>
<div class="copyright">© Copyright 2014 - Company name</div>
</body>
</html>
```